2 sets of Business cards, stationary/envelopes, stationary template(MS Word), door hang tag
KRV Building Works, LLC (Design A) and Steadfield Estate Holdings, LLC (Design B)
2 sets of Business cards, stationary/envelopes, stationary template(MS Word), door hang tag - Real Estate
Creative Brief
Simple
Darrel K. Winton
Managing Member
5120 Larkspur Lane, Suite B Columbia, MO 65201
Don't know yet, but need space for it
dwinton@krvbuildworks.com
www.krvbuildworks.com (Design A) and www.steadfieldleasing.com (Design B)
We are a family owned business with 90+ years in the construction and real estate sector and would like to present our company as a quality, professional organization with a sleek modern set of stationary. Stationary design A: Company name: KRV Building Works, LLC Optional Tagline: Working from experience, not for it! Color Mode: RGB color Grey :R=149 G=149 B=149 White: R=255 G=255 B=255 Black : R=0 G=0 B=0 Blue : R=0 G=97 B=240 dwinton@krvbuildworks.com (Design A) For: KRV Building Works, LLC Stationary design B: Company name: Steadfield Estate Holdings, LLC Optional Tagline: Steadfield Precision, Steadfield Dedication Color Mode: RGB color Grey :R=149 G=149 B=149 White: R=255 G=255 B=255 Black : R=0 G=0 B=0 Red : R=209 G=0 B=0 dwinton@steadfieldleasing.com (Design B) For: Steadfield Estate Holdings, LLC Phone, email, and name will change for the additional members of the company. We also want an electronic email signature, and digital stationary template (MS word). Stationary and envelopes should tie in the theme of the business cards for a uniform look. Also looking for a Header only version of the stationary, as well as a full page version (header and footer used for design).
Logo used in a creative way.
darrelkwinton darrelkwinton
Sorry, been out of the office. Waiting for partners to look at everything before making comments. We should be leaving comments and making recommendations in the next day or two for all of the designs we want to see refined. Thanks, Darrel

```html
<!DOCTYPE html>
<html lang="en">
<head>
<meta charset="utf-8">
<title>KRV Building Works – Business Card</title>
<link rel="stylesheet" href="https://fonts.googleapis.com/css2?family=Questrial&display=swap">
<style>
  :root {
    --bg: #e9e9e9;
    --white: #ffffff;
    --black: #000000;
    --grey: #959595;
    --grey-dark: #3a3a3a;
    --blue: #0061f0;
    --text: #4a4a4a;
  }
  * { margin: 0; padding: 0; box-sizing: border-box; }
  html, body { width: 1200px; height: 901px; overflow: hidden; }
  body {
    background: var(--bg);
    font-family: "Questrial", "Century Gothic", sans-serif;
    position: relative;
  }
  .card {
    position: absolute;
    left: 250px;
    width: 700px;
    height: 400px;
    overflow: hidden;
    box-shadow: 0 6px 18px rgba(0,0,0,.18);
  }
  .card--back { top: 30px; background: var(--black); }
  .card--front { top: 470px; background: var(--white); }

  .back-pattern {
    position: absolute; inset: 0;
    background: radial-gradient(ellipse at 55% 45%, #2e2e2e 0%, #161616 55%, #080808 100%);
  }
  .back-mark {
    position: absolute; left: 0; right: 0; top: 186px;
    display: flex; justify-content: center; align-items: center; gap: 10px;
    color: var(--white); font-size: 20px; letter-spacing: 1px;
  }
  .back-mark .square { width: 14px; height: 14px; background: var(--blue); }

  .front-base { position: absolute; inset: 0; }

  .brand {
    position: absolute; left: 48px; top: 118px;
    display: flex; align-items: center; gap: 16px;
  }
  .brand .square { width: 46px; height: 46px; background: var(--blue); }
  .brand .name {
    color: var(--grey-dark); font-size: 30px; line-height: 1.05; letter-spacing: .5px;
  }

  .contact {
    position: absolute; left: 430px; top: 40px; width: 250px;
    color: var(--text); font-size: 13px; line-height: 1.35;
  }
  .contact .person { color: var(--blue); font-size: 19px; line-height: 1.2; }
  .contact .role { font-size: 13px; margin-bottom: 14px; }
  .contact .address { margin-bottom: 12px; }
  .phones { list-style: none; }
  .phones li { display: flex; align-items: center; gap: 8px; height: 18px; }
  .phones svg { width: 12px; height: 12px; flex: none; }
  .contact .email { margin-top: 2px; }

  .website {
    position: absolute; right: 36px; bottom: 26px;
    color: var(--white); font-size: 14px; letter-spacing: .5px;
  }
</style>
</head>
<body>

  <section class="card card--back" aria-label="Card back">
    <div class="back-pattern" role="img" aria-label="Dark repeating geometric background pattern"></div>
    <div class="back-mark"><span class="square"></span><span>KRV Building Works</span></div>
  </section>

  <section class="card card--front" aria-label="Card front">
    <svg class="front-base" viewBox="0 0 700 400" preserveAspectRatio="none" aria-hidden="true">
      <path d="M0 342 C 200 322, 430 290, 700 280 L700 400 L0 400 Z" fill="var(--black)"/>
      <path d="M0 332 C 200 312, 430 280, 700 270" fill="none" stroke="var(--blue)" stroke-width="3"/>
      <path d="M0 338 C 200 318, 430 286, 700 276" fill="none" stroke="var(--grey)" stroke-width="1"/>
    </svg>

    <div class="brand">
      <span class="square"></span>
      <span class="name">KRV Building Works</span>
    </div>

    <div class="contact">
      <div class="person">Darrel K. Winton</div>
      <div class="role">Managing Member</div>
      <div class="address">5120 Larkspur Lane, Suite B<br>Columbia, MO 65201</div>
      <ul class="phones">
        <li>
          <svg viewBox="0 0 12 12"><path d="M2 1h2l1 3-1.5 1a6 6 0 0 0 3.5 3.5L8 7l3 1v2a1 1 0 0 1-1 1A9 9 0 0 1 1 2a1 1 0 0 1 1-1z" fill="var(--blue)"/></svg>
          (999) 999-9999
        </li>
        <li>
          <svg viewBox="0 0 12 12"><path d="M2 1h2l1 3-1.5 1a6 6 0 0 0 3.5 3.5L8 7l3 1v2a1 1 0 0 1-1 1A9 9 0 0 1 1 2a1 1 0 0 1 1-1z" fill="var(--blue)"/></svg>
          (999) 999-9999
        </li>
        <li>
          <svg viewBox="0 0 12 12"><rect x="1" y="4" width="10" height="7" rx="1" fill="var(--blue)"/><rect x="3" y="1" width="6" height="4" fill="var(--blue)"/></svg>
          (573) 555-0142
        </li>
        <li>
          <svg viewBox="0 0 12 12"><rect x="3" y="0.5" width="6" height="11" rx="1.2" fill="var(--blue)"/><rect x="4" y="2" width="4" height="6" fill="var(--white)"/></svg>
          (573) 555-0187
        </li>
      </ul>
      <div class="email">dwinton@krvbuildworks.com</div>
    </div>

    <div class="website">www.krvbuildworks.com</div>
  </section>

</body>
</html>
```